I need an Oakline Office selling website

My Oakline Office store is driven by creativity and innovation. With this i am searching for an industry standard website for my Oakline Office and items selling website. I sell a wide range of Oakline Office items such as chairs, tables, burglary, cotton, wardrobe, etc. There will be a category for each of the items i sell. My business is based in the United States and services only US based residents. I don't accept online payments and customers are to pay on delivery of items. The website is to have images of the items i sell. I would like brown, black and golden colors because those are the colors furniture mostly make use of. Designs submitted should be unique.

Industry/Entity Type

Furniture Store

Coding

Coded - Design and coding required

```html
<!DOCTYPE html>
<html lang="en">
<head>
<meta charset="utf-8">
<title>Oakline Office</title>
<link rel="stylesheet" href="https://fonts.googleapis.com/css2?family=Oswald:wght@300;400&family=Open+Sans:wght@300;400;600;700&display=swap">
<style>
  :root {
    --ink: #2a1d14;
    --text: #5a4a3e;
    --line: #d3c3a4;
    --gold: #b8913f;
    --gold-soft: #e3cf9f;
    --panel: #f2ebdd;
    --white: #ffffff;
    --brown: #3b2a1f;
    --brown-deep: #2b1e16;
  }
  * { margin: 0; padding: 0; box-sizing: border-box; }
  html, body { width: 703px; height: 1200px; overflow: hidden; background: var(--white); }
  body { position: relative; font-family: "Open Sans", Arial, sans-serif; color: var(--ink); }
  .abs { position: absolute; }

  /* header */
  .social-ring { position: absolute; width: 30px; height: 30px; border-radius: 50%; border: 1px solid var(--line); display: flex; align-items: center; justify-content: center; }
  .social-ring svg { display: block; }
  .social-ring.strong { border-color: var(--ink); }
  .social-ring.filled { background: var(--brown); border-color: var(--brown); }
  .brand { left: 0; width: 703px; top: 12px; text-align: center; font-family: "Oswald", "Arial Narrow", sans-serif; font-weight: 300; font-size: 31px; letter-spacing: 0.5px; line-height: 40px; }
  .call-icon { left: 502px; top: 18px; width: 34px; height: 34px; border-radius: 50%; border: 1.5px solid var(--gold); display: flex; align-items: center; justify-content: center; }
  .call-label { left: 543px; top: 14px; font-size: 12.5px; font-weight: 300; line-height: 16px; }
  .call-number { left: 542px; top: 29px; font-size: 19.5px; font-weight: 700; line-height: 24px; color: var(--brown); }
  .rule-double { left: 45px; width: 613px; top: 66px; height: 4px; border-top: 1px solid var(--gold); border-bottom: 1px solid var(--gold); }

  .main-nav { left: 48px; top: 76px; height: 16px; font-size: 11.5px; font-weight: 300; }
  .main-nav a { position: absolute; color: var(--ink); text-decoration: none; white-space: nowrap; }

  .hero { left: 45px; top: 99px; width: 613px; height: 305px; background: linear-gradient(180deg, #ece8e0 0%, #d2cbbd 45%, #6f6258 75%, #3f332b 100%); }

  /* feature grid */
  .tile { position: absolute; width: 204.5px; height: 140px; }
  .tile.photo-logo { background: radial-gradient(circle at 50% 50%, #f7efd9 0%, #e6d3a5 60%, #c4a56a 100%); }
  .tile.photo-desk { background: linear-gradient(160deg, #ece9e2 0%, #c9c0b0 50%, #6b4a38 75%, #9a8c7c 100%); }
  .tile.photo-chair { background: linear-gradient(180deg, #f4f1e8 0%, #ddd4c0 45%, #4a3f37 70%, #c99a6a 100%); }
  .tile.copy { background: var(--panel); text-align: center; padding-top: 14px; }
  .tile-title { font-size: 26px; font-weight: 300; line-height: 32px; letter-spacing: 0.3px; }
  .tile-text { font-size: 9.6px; line-height: 14.5px; color: var(--text); width: 184px; margin: 4px auto 0; }
  .btn { display: inline-flex; align-items: center; gap: 4px; background: var(--brown); color: var(--white); font-size: 12px; height: 30px; padding: 0 13px; margin-top: 7px; border-bottom: 2px solid var(--gold); }

  /* contact */
  .contact { left: 45px; top: 746px; width: 613px; height: 262px; background: linear-gradient(135deg, #3a2a1f 0%, #2b1e16 55%, #35261c 100%); }
  .contact-title { left: 0; width: 703px; top: 776px; text-align: center; color: var(--white); font-size: 25px; font-weight: 300; line-height: 32px; }
  .field { position: absolute; border: 1px solid var(--gold-soft); color: var(--white); font-size: 9.5px; padding: 6px 6px; line-height: 14px; }
  .submit { left: 306px; top: 938px; width: 92px; height: 30px; background: var(--gold); color: var(--white); font-size: 13px; display: flex; align-items: center; justify-content: center; }

  /* footer */
  .foot-col { position: absolute; top: 1032px; }
  .foot-title { font-size: 14px; font-weight: 300; line-height: 18px; margin-bottom: 8px; }
  .foot-links { list-style: none; font-size: 9.5px; color: var(--text); line-height: 16px; }
  .foot-text { font-size: 9.5px; color: var(--text); line-height: 15px; }
  .news-input { position: absolute; left: 204px; top: 1092px; width: 138px; height: 21px; border: 1px solid var(--line); font-size: 9.5px; color: var(--text); padding: 3px; }
  .subscribe { left: 204px; top: 1120px; width: 89px; height: 27px; background: var(--brown); color: var(--white); font-size: 12px; display: flex; align-items: center; justify-content: center; }
  .touch-row { position: absolute; left: 364px; display: flex; gap: 6px; font-size: 9.5px; color: var(--text); line-height: 15px; }
  .touch-row svg { flex: none; margin-top: 1px; }
  .touch-row.bold { font-weight: 600; }
  .rule-foot { left: 45px; width: 614px; top: 1165px; border-top: 1px solid var(--line); }
  .copyright { left: 0; width: 703px; top: 1174px; text-align: center; font-size: 9.5px; color: var(--text); }
  .copyright strong { color: var(--ink); font-weight: 700; }
</style>
</head>
<body>

<header>
  <span class="social-ring strong" style="left:45px;top:21px" role="img" aria-label="Share">
    <svg width="13" height="13" viewBox="0 0 14 14"><circle cx="3" cy="7" r="2" fill="#2a1d14"/><circle cx="11" cy="3" r="2" fill="#2a1d14"/><circle cx="11" cy="11" r="2" fill="#2a1d14"/><path d="M3 7L11 3M3 7l8 4" stroke="#2a1d14" stroke-width="1.2"/></svg>
  </span>
  <span class="social-ring" style="left:88px;top:21px" role="img" aria-label="Chat">
    <svg width="13" height="12" viewBox="0 0 14 13"><path d="M1 1h12v8H6l-3 3V9H1z" fill="#b9ab95"/></svg>
  </span>
  <span class="social-ring" style="left:131px;top:21px" role="img" aria-label="Website">
    <svg width="13" height="13" viewBox="0 0 14 14"><circle cx="7" cy="7" r="5.8" fill="none" stroke="#b9ab95" stroke-width="1.2"/><path d="M1.2 7h11.6M7 1.2c-2.5 3-2.5 8.6 0 11.6M7 1.2c2.5 3 2.5 8.6 0 11.6" fill="none" stroke="#b9ab95" stroke-width="1"/></svg>
  </span>

  <div class="abs brand">OAKLINE OFFICE</div>

  <div class="abs call-icon">
    <svg width="16" height="16" viewBox="0 0 24 24"><path fill="#2a1d14" d="M6.6 10.8a15.1 15.1 0 0 0 6.6 6.6l2.2-2.2c.3-.3.7-.4 1-.2 1.1.4 2.3.6 3.6.6.6 0 1 .4 1 1V20c0 .6-.4 1-1 1A17 17 0 0 1 3 4c0-.6.4-1 1-1h3.5c.6 0 1 .4 1 1 0 1.3.2 2.5.6 3.6.1.3 0 .7-.2 1z"/></svg>
  </div>
  <div class="abs call-label">CALL US NOW</div>
  <div class="abs call-number">555 010 2468</div>
  <div class="abs rule-double"></div>

  <nav class="abs main-nav">
    <a style="left:0">HOME</a>
    <a style="left:71px">ABOUT</a>
    <a style="left:145px">PRODUCTS</a>
    <a style="left:241px">SPECIALS</a>
    <a style="left:327px">NEWS</a>
    <a style="left:397px">CONTACT</a>
  </nav>
</header>

<div class="abs hero" role="img" aria-label="Photo of a bright conference room with a long dark table and black office chairs"></div>

<section class="features">
  <div class="tile photo-logo" style="left:45px;top:435px" role="img" aria-label="Photo of a light meeting room with the store emblem"></div>
  <div class="tile copy" style="left:249.5px;top:435px">
    <div class="tile-title">SPECIAL</div>
    <p class="tile-text">Lorem Ipsum is simply dummy text of the printing and typesetting industry. Lorem Ipsum has been the industry.</p>
    <span class="btn">READ MORE <svg width="8" height="11" viewBox="0 0 8 11"><path d="M1.5 1l5 4.5-5 4.5" fill="none" stroke="#fff" stroke-width="2"/></svg></span>
  </div>
  <div class="tile photo-desk" style="left:454px;top:435px" role="img" aria-label="Photo of an executive desk with a wooden top in a glass office"></div>

  <div class="tile copy" style="left:45px;top:576px">
    <div class="tile-title">WELCOME</div>
    <p class="tile-text">Lorem Ipsum is simply dummy text of the printing and typesetting industry. Lorem Ipsum has been the industry.</p>
    <span class="btn">READ MORE <svg width="8" height="11" viewBox="0 0 8 11"><path d="M1.5 1l5 4.5-5 4.5" fill="none" stroke="#fff" stroke-width="2"/></svg></span>
  </div>
  <div class="tile photo-chair" style="left:249.5px;top:576px" role="img" aria-label="Photo of a grey shell chair with wooden legs at a home office desk"></div>
  <div class="tile copy" style="left:454px;top:576px">
    <div class="tile-title">PRODUCTS</div>
    <p class="tile-text">Lorem Ipsum is simply dummy text of the printing and typesetting industry. Lorem Ipsum has been the industry.</p>
    <span class="btn">VIEW ALL <svg width="8" height="11" viewBox="0 0 8 11"><path d="M1.5 1l5 4.5-5 4.5" fill="none" stroke="#fff" stroke-width="2"/></svg></span>
  </div>
</section>

<section>
  <div class="abs contact" role="img" aria-label="Dimmed photo of a desk with a laptop and a plant"></div>
  <h2 class="abs contact-title">CONTACT US</h2>
  <div class="field" style="left:132px;top:818px;width:195px;height:27px">Enter Name</div>
  <div class="field" style="left:132px;top:858px;width:195px;height:27px">Enter Email</div>
  <div class="field" style="left:132px;top:898px;width:195px;height:27px">Enter Contact No.</div>
  <div class="field" style="left:340px;top:818px;width:231px;height:107px">Enter Message</div>
  <div class="abs submit">SUBMIT</div>
</section>

<footer>
  <div class="foot-col" style="left:46px">
    <div class="foot-title">Useful Links</div>
    <ul class="foot-links">
      <li>Home</li><li>About</li><li>Products</li><li>Specials</li><li>News</li><li>Contact</li>
    </ul>
  </div>

  <div class="foot-col" style="left:205px">
    <div class="foot-title">Newsletter</div>
    <p class="foot-text" style="width:130px">Subscribe to stay on Oakline Office</p>
  </div>
  <div class="news-input">Enter Email Id</div>
  <div class="abs subscribe">SUBSCRIBE</div>

  <div class="foot-col" style="left:364px">
    <div class="foot-title">Get In Touch</div>
  </div>
  <div class="touch-row" style="top:1058px">
    <svg width="9" height="12" viewBox="0 0 9 12"><path d="M4.5 0A4.5 4.5 0 0 0 0 4.5C0 8 4.5 12 4.5 12S9 8 9 4.5A4.5 4.5 0 0 0 4.5 0zm0 6.3a1.8 1.8 0 1 1 0-3.6 1.8 1.8 0 0 1 0 3.6z" fill="#2a1d14"/></svg>
    <span style="width:125px">Lorem Ipsum is simply dummy text of the printing</span>
  </div>
  <div class="touch-row bold" style="top:1092px">
    <svg width="11" height="11" viewBox="0 0 24 24"><path fill="#2a1d14" d="M6.6 10.8a15.1 15.1 0 0 0 6.6 6.6l2.2-2.2c.3-.3.7-.4 1-.2 1.1.4 2.3.6 3.6.6.6 0 1 .4 1 1V20c0 .6-.4 1-1 1A17 17 0 0 1 3 4c0-.6.4-1 1-1h3.5c.6 0 1 .4 1 1 0 1.3.2 2.5.6 3.6.1.3 0 .7-.2 1z"/></svg>
    <span>555 010 2468</span>
  </div>
  <div class="touch-row" style="top:1115px">
    <svg width="11" height="9" viewBox="0 0 11 9"><rect x="0.5" y="0.5" width="10" height="8" fill="none" stroke="#2a1d14"/><path d="M0.5 0.8l5 4 5-4" fill="none" stroke="#2a1d14"/></svg>
    <span>hello@oaklineoffice.example</span>
  </div>

  <div class="foot-col" style="left:522px">
    <div class="foot-title">Connect With Us</div>
  </div>
  <span class="social-ring filled" style="left:521px;top:1059px" role="img" aria-label="Share">
    <svg width="13" height="13" viewBox="0 0 14 14"><circle cx="3" cy="7" r="2" fill="#e3cf9f"/><circle cx="11" cy="3" r="2" fill="#e3cf9f"/><circle cx="11" cy="11" r="2" fill="#e3cf9f"/><path d="M3 7L11 3M3 7l8 4" stroke="#e3cf9f" stroke-width="1.2"/></svg>
  </span>
  <span class="social-ring" style="left:563px;top:1059px" role="img" aria-label="Chat">
    <svg width="13" height="12" viewBox="0 0 14 13"><path d="M1 1h12v8H6l-3 3V9H1z" fill="#b9ab95"/></svg>
  </span>
  <span class="social-ring" style="left:606px;top:1059px" role="img" aria-label="Website">
    <svg width="13" height="13" viewBox="0 0 14 14"><circle cx="7" cy="7" r="5.8" fill="none" stroke="#b9ab95" stroke-width="1.2"/><path d="M1.2 7h11.6M7 1.2c-2.5 3-2.5 8.6 0 11.6M7 1.2c2.5 3 2.5 8.6 0 11.6" fill="none" stroke="#b9ab95" stroke-width="1"/></svg>
  </span>

  <div class="abs rule-foot"></div>
  <p class="abs copyright">© <strong>OAKLINE OFFICE</strong> - 2016. All Rights Reserved.</p>
</footer>

</body>
</html>
```